business stationery for email layout
startup company
Simple
RT
Via G. Morelli, 17
26813 Castelverna CV
Italy
Info@Tallimora.com
www.tallimora.com
minimalist, retail, fashion, technology, internet, innovative,one-step ahead, easy, intuitive, immediate, serious,credible
logo blue version
logo grey version
symbol blue version
symbol grey version

```html
<!DOCTYPE html>
<html lang="it">
<head>
<meta charset="utf-8">
<title>Tallimora – Business Card</title>
<link rel="stylesheet" href="https://fonts.googleapis.com/css2?family=Open+Sans:wght@400;600;700&display=swap">
<style>
  :root {
    --backdrop: #383838;
    --card: #ffffff;
    --ink: #3a3a3a;
    --brand-deep: #2c4f9e;
    --brand-light: #1ba3cf;
    --rule: #555555;
  }
  * { margin: 0; padding: 0; box-sizing: border-box; }
  html, body {
    width: 1200px;
    height: 902px;
    overflow: hidden;
    background: var(--backdrop);
    font-family: "Open Sans", Arial, sans-serif;
    color: var(--ink);
  }
  .card {
    position: absolute;
    left: 113px;
    top: 183px;
    width: 932px;
    height: 535px;
    background: var(--card);
  }
  .brand-circle {
    position: absolute;
    left: 648px;
    top: 24px;
    width: 220px;
    height: 220px;
    border-radius: 50%;
    background: linear-gradient(135deg, var(--brand-deep) 0%, var(--brand-light) 100%);
  }
  .wordmark {
    position: absolute;
    left: 30px;
    top: 412px;
    font-size: 63px;
    font-weight: 600;
    letter-spacing: 1px;
    color: var(--brand-deep);
    line-height: 1;
  }
  .divider {
    position: absolute;
    left: 422px;
    top: 359px;
    width: 2px;
    height: 147px;
    background: var(--rule);
  }
  .contact {
    position: absolute;
    left: 441px;
    top: 356px;
    font-size: 16px;
    line-height: 25px;
  }
  .contact .initials {
    font-size: 25px;
    font-weight: 400;
    line-height: 32px;
    margin-bottom: -2px;
  }
  .contact .label { font-weight: 700; }
</style>
</head>
<body>
  <main class="card">
    <div class="brand-circle" role="img" aria-label="Tallimora brand symbol area"></div>
    <div class="wordmark">TALLIMORA</div>
    <div class="divider"></div>
    <div class="contact">
      <p class="initials">RT</p>
      <p><span class="label">P:</span> +390287614320</p>
      <p><span class="label">F:</span> +390287614391</p>
      <p><span class="label">E:</span> Info@Tallimora.com</p>
      <p><span class="label">W:</span> www.tallimora.com</p>
      <p class="address">Via G. Morelli, 17 26813 Castelverna CV Italy</p>
    </div>
  </main>
</body>
</html>
```